2022 Grenache Hillside Vineyard Sketch Wine Label

Size:4"X4"
Wine: 2022 Grenache
Vineyard Name: Low Mill Vineyard
AVA: Solano County
Alcohol by Volume:15%
Volume:750ml
Must Feature a hillside vineyard on the label somehow, I picture it being a sketch but it doesn't have to be. Not looking for anything flashy or colorful but maybe a pop of color somewhere. I am not yet sure that I want to include our name, but you can try to work in "KMT" somewhere on the label if it fits the design.
The Label must include all the information listed above. The Grenache was grown in a hillside vineyard, so I wanted the label to prominently feature a hillside vineyard. You can layout the label however you see best, but the vintage and varietal should be prominent, the ABV can be in small type face but must be legible following FQD guidelines. If you are able to make the vineyard name pop as well that would be good.
You don't have to use these, but our standard fonts we use are:
For Varietal: Bianca
Secondary (vintage, AVA, Vineyard):Helvetica
ABV/Volume: PT Serif
Thank you, look forward to the results

```html
<!DOCTYPE html>
<html lang="en">
<head>
<meta charset="utf-8">
<title>Grenache 2022 – Wine Label</title>
<link href="https://fonts.googleapis.com/css2?family=Bebas+Neue&family=Raleway:wght@300;400&family=Pinyon+Script&display=swap" rel="stylesheet">
<style>
  :root {
    --backdrop: #1f1f1f;
    --label-light: #fbfbf9;
    --label-shade: #dcdedb;
    --ink-dark: #2b2b2b;
    --vintage-red: #a50f12;
    --brand-red: #c8161b;
    --detail-grey: #5a5a5a;
    --script-grey: #8a8a8a;
    --sketch-olive: #6e7560;
    --sketch-mid: #a7ac9c;
    --sketch-pale: #d6d9cf;
  }
  * { margin: 0; padding: 0; box-sizing: border-box; }
  html, body {
    width: 1200px;
    height: 2171px;
    overflow: hidden;
    background: var(--backdrop);
  }
  .canvas {
    position: relative;
    width: 1200px;
    height: 2171px;
    background: var(--backdrop);
  }
  .label {
    position: absolute;
    left: 100px;
    top: 585px;
    width: 1000px;
    height: 1000px;
    background: linear-gradient(90deg, var(--label-light) 0%, #f2f3f1 35%, var(--label-shade) 100%);
    overflow: hidden;
  }
  .varietal {
    position: absolute;
    right: 62px;
    top: 78px;
    font-family: "Bebas Neue", "Oswald", sans-serif;
    font-weight: 400;
    font-size: 212px;
    line-height: 1;
    color: var(--ink-dark);
    letter-spacing: 1px;
  }
  .vintage {
    position: absolute;
    right: 62px;
    top: 258px;
    font-family: "Bebas Neue", "Oswald", sans-serif;
    font-size: 86px;
    line-height: 1;
    color: var(--vintage-red);
    letter-spacing: 5px;
  }
  .vineyard-sketch {
    position: absolute;
    left: 4px;
    top: 249px;
    width: 681px;
    height: 505px;
    background: linear-gradient(165deg, var(--sketch-mid) 0%, var(--sketch-olive) 45%, var(--sketch-mid) 75%, var(--sketch-pale) 100%);
    opacity: 0.75;
    -webkit-mask-image: radial-gradient(ellipse 60% 58% at 42% 55%, #000 55%, transparent 100%);
    mask-image: radial-gradient(ellipse 60% 58% at 42% 55%, #000 55%, transparent 100%);
  }
  .details {
    position: absolute;
    right: 64px;
    text-align: right;
    line-height: 1;
  }
  .abv {
    top: 734px;
    font-family: "Raleway", sans-serif;
    font-weight: 300;
    font-size: 40px;
    font-variant: small-caps;
    color: var(--detail-grey);
  }
  .ava {
    top: 786px;
    right: 66px;
    font-family: "Pinyon Script", cursive;
    font-size: 58px;
    color: var(--script-grey);
  }
  .volume {
    top: 874px;
    font-family: "Raleway", sans-serif;
    font-weight: 300;
    font-size: 40px;
    font-variant: small-caps;
    color: var(--detail-grey);
  }
  .brand-name {
    position: absolute;
    left: 52px;
    top: 810px;
    width: 380px;
    font-family: "Bebas Neue", "Oswald", sans-serif;
    font-size: 58px;
    line-height: 0.92;
    color: var(--brand-red);
    letter-spacing: 3px;
  }
</style>
</head>
<body>
<main class="canvas">
  <section class="label">
    <h1 class="varietal">GRENACHE</h1>
    <p class="vintage">2022</p>
    <div class="vineyard-sketch" role="img" aria-label="Olive pen sketch of a hillside vineyard, rows of vines sweeping up to a hilltop village"></div>
    <p class="details abv">alc.15%</p>
    <p class="details ava">Solano County</p>
    <p class="details volume">750ml.</p>
    <p class="brand-name">Low Mill<br>Vineyard</p>
  </section>
</main>
</body>
</html>
```